Business Card Design Project

We need a business card design for an existing company in Dallas/Fort Worth that is expanding services and re-branding. We are changing the name from Brightmoor Commercial Cleaning to Keystride Facility Services. We are expanding from only commercial cleaning to include complete commercial landscape and facility maintenance services, too.

As stated, we offer a package of services that includes landscape, janitorial and facility services, which is largely unique in the industry.

We would like a design that communicates trust/partnership with a professional, corporate image, but not necessarily using the standard white business card. We would like a design that perhaps uses darker blues or perhaps a gray background, but we are open to other ideas. We might also be interested in a double-sided design - maybe with our logo on the back, printed on a gray background?

We will probably stick with the attached logo, but if you've got another inspired idea....

Target Market(s)

Property managers, commercial real estate professionals, corporate executives

Industry/Entity Type

Landscape

Requirements
Should not have
• Not interested in old style fonts.

```html
<!DOCTYPE html>
<html lang="en">
<head>
<meta charset="utf-8">
<title>Keystride Facility Services – Business Card</title>
<link rel="stylesheet" href="https://fonts.googleapis.com/css2?family=Questrial&family=Open+Sans:ital,wght@1,400&family=Arimo&display=swap">
<style>
  :root {
    --ink: #000000;
    --paper: #ffffff;
    --card-glow: #3b3b3b;
    --card-edge: #050505;
    --type: #ffffff;
  }
  html, body {
    margin: 0;
    padding: 0;
    overflow: hidden;
    background: var(--ink);
  }
  .canvas {
    position: relative;
    width: 1041px;
    height: 1200px;
    background: var(--ink);
    overflow: hidden;
  }
  .sheet {
    position: absolute;
    left: 41px;
    top: 34px;
    width: 959px;
    height: 1125px;
    background: var(--paper);
  }
  .card {
    position: absolute;
    background: radial-gradient(ellipse at 50% 62%, var(--card-glow) 0%, #1a1a1a 45%, var(--card-edge) 100%);
    color: var(--type);
  }
  .card-front {
    left: 84px;
    top: 81px;
    width: 865px;
    height: 495px;
  }
  .brand {
    position: absolute;
    left: 49px;
    top: 160px;
    display: flex;
    align-items: flex-start;
  }
  .brand-square {
    width: 117px;
    height: 117px;
    border: 8px solid var(--type);
    flex: none;
  }
  .brand-text {
    margin-left: 16px;
    width: 630px;
  }
  .brand-name {
    font-family: "Questrial", "Century Gothic", sans-serif;
    font-weight: 400;
    color: var(--type);
    text-transform: uppercase;
    line-height: 1;
    margin: 0;
    white-space: nowrap;
  }
  .brand-name .line-1 {
    display: block;
    font-size: 72px;
    letter-spacing: 21px;
  }
  .brand-name .line-2 {
    display: block;
    font-size: 46px;
    letter-spacing: 12px;
    margin-top: 2px;
  }
  .tagline {
    font-family: "Open Sans", Arial, sans-serif;
    font-style: italic;
    font-size: 22px;
    margin: 2px 0 0 2px;
    white-space: nowrap;
  }
  .contact {
    position: absolute;
    left: 0;
    right: 0;
    top: 405px;
    text-align: center;
    font-family: "Arimo", Arial, sans-serif;
    font-size: 25px;
    line-height: 30px;
    margin: 0;
    white-space: nowrap;
  }
  .card-back {
    left: 80px;
    top: 613px;
    width: 866px;
    height: 492px;
    background: var(--ink);
  }
  .back-frame {
    position: absolute;
    inset: 15px;
    border: 12px solid var(--paper);
    background: var(--ink);
  }
  .back-panel {
    position: absolute;
    inset: 6px;
    background: radial-gradient(ellipse at 50% 48%, var(--card-glow) 0%, #181818 50%, var(--card-edge) 100%);
    display: flex;
    align-items: center;
    justify-content: center;
    gap: 28px;
  }
  .back-square {
    width: 90px;
    height: 90px;
    border: 10px solid var(--type);
  }
  .back-name {
    font-family: "Questrial", "Century Gothic", sans-serif;
    font-weight: 400;
    color: var(--type);
    text-transform: uppercase;
    font-size: 54px;
    letter-spacing: 5px;
    line-height: 1.05;
    margin: 0;
  }
</style>
</head>
<body>
<div class="canvas">
  <div class="sheet"></div>

  <section class="card card-front">
    <div class="brand">
      <div class="brand-square"></div>
      <div class="brand-text">
        <h1 class="brand-name"><span class="line-1">Keystride</span><span class="line-2">Facility Services</span></h1>
        <p class="tagline">Complete Care For Grounds, Cleaning and Building Upkeep</p>
      </div>
    </div>
    <p class="contact">
      Marlin Court 48 &nbsp;I&nbsp; 5820 Cedarvale, TX &nbsp;I&nbsp; T.&nbsp; 00 000 00 00 &nbsp;I&nbsp; F.&nbsp; 00 000 00 00<br>
      E.&nbsp; info@keystridefs.com &nbsp;I&nbsp; W. www.keystridefacilityservices.com
    </p>
  </section>

  <section class="card card-back">
    <div class="back-frame">
      <div class="back-panel">
        <div class="back-square"></div>
        <p class="back-name">Keystride</p>
      </div>
    </div>
  </section>
</div>
</body>
</html>
```